Book Cover for Christian Book titled, "Lamps Along the Quiet Road"

Size of book cover will be 6" x 9".
The book is about how a person can know beyond a shadow of a doubt that they will go to heaven when they die.
The Title is "Lamps Along the Quiet Road"
Subtitle is "A Plain Guide to Lasting Peace and Steady Hope for Every Season."
The front of the book should have title, subtitle, and author. The back of the book and spine should have no text and be a solid color.
The uploaded pic is a possibility for a design; but I'm open to other designs.
Whatever images are used need to be very high quality to meet Maple Print Works guidelines. Also, the finished product needs to be sized to match the MPW guide for a 6x9 book.

```html
<!DOCTYPE html>
<html lang="en">
<head>
<meta charset="utf-8">
<title>Lamps Along the Quiet Road — Cover Spread</title>
<link rel="stylesheet" href="https://fonts.googleapis.com/css2?family=Playfair+Display:wght@500;600&family=Fraunces:wght@400&display=swap">
<style>
  :root {
    --paper: #ffffff;
    --back-teal: #52bdd3;
    --guide: #1a1a1a;
    --title-deep: #274a8c;
    --title-teal: #1b8fa8;
    --subtitle-ink: #2b4a8a;
    --band-yellow: #f3e862;
    --sky-white: #ffffff;
    --sky-haze: #e8edf1;
    --sun-gold: #f2ea7e;
    --field-green: #2f8a35;
    --field-dark: #1f6a26;
  }
  html, body {
    margin: 0;
    padding: 0;
    width: 1200px;
    height: 1096px;
    overflow: hidden;
    background: var(--paper);
  }
  .spread {
    position: absolute;
    left: 114px;
    top: 201px;
    width: 982px;
    height: 702px;
  }
  .back-and-spine {
    position: absolute;
    left: 0;
    top: 0;
    width: 517px;
    height: 702px;
    background: var(--back-teal);
  }
  .front-cover {
    position: absolute;
    left: 517px;
    top: 0;
    width: 465px;
    height: 702px;
    overflow: hidden;
  }
  .cover-scene {
    position: absolute;
    inset: 0;
    background: linear-gradient(to bottom,
      var(--sky-white) 0%,
      var(--sky-white) 24%,
      var(--sky-haze) 42%,
      var(--sun-gold) 70%,
      var(--sun-gold) 80%,
      var(--field-green) 84%,
      var(--field-dark) 100%);
  }
  .cover-title {
    position: absolute;
    left: 0;
    top: 0;
    width: 465px;
    height: 702px;
  }
  .subtitle-band {
    position: absolute;
    left: 41px;
    top: 270px;
    width: 378px;
    height: 57px;
    background: var(--band-yellow);
    filter: blur(3px);
    opacity: 0.95;
  }
  .subtitle {
    position: absolute;
    left: 56px;
    top: 282px;
    width: 348px;
    margin: 0;
    text-align: center;
    font-family: "Fraunces", Georgia, serif;
    font-size: 13.5px;
    line-height: 17px;
    letter-spacing: 0.5px;
    color: var(--subtitle-ink);
  }
  .trim-guides {
    position: absolute;
    left: 0;
    top: 0;
    width: 982px;
    height: 702px;
    pointer-events: none;
  }
</style>
</head>
<body>
  <div class="spread">
    <div class="back-and-spine" aria-label="Back cover and spine, solid colour"></div>

    <section class="front-cover">
      <div class="cover-scene" role="img" aria-label="Photograph of a bright sun breaking through clouds over a wide green field at the horizon"></div>

      <svg class="cover-title" viewBox="0 0 465 702" aria-label="Lamps Along the Quiet Road">
        <defs>
          <linearGradient id="titleInk" x1="0" y1="0" x2="1" y2="1">
            <stop offset="0" stop-color="var(--title-teal)"/>
            <stop offset="0.45" stop-color="var(--title-deep)"/>
            <stop offset="0.75" stop-color="var(--title-teal)"/>
            <stop offset="1" stop-color="var(--title-deep)"/>
          </linearGradient>
        </defs>
        <g font-family="Playfair Display, Georgia, serif" fill="url(#titleInk)" text-anchor="middle">
          <text x="231" y="97" font-size="42" font-weight="500" textLength="328" lengthAdjust="spacingAndGlyphs">LAMPS ALONG</text>
          <text x="231" y="157" font-size="64" font-weight="500" textLength="330" lengthAdjust="spacingAndGlyphs">THE QUIET</text>
          <text x="231" y="255" font-size="118" font-weight="600" textLength="332" lengthAdjust="spacingAndGlyphs">ROAD</text>
        </g>
      </svg>

      <div class="subtitle-band"></div>
      <p class="subtitle">A Plain Guide to Lasting Peace and Steady Hope for Every Season.</p>
    </section>

    <svg class="trim-guides" viewBox="0 0 982 702" aria-hidden="true">
      <g fill="none" stroke="var(--guide)" stroke-width="0.8">
        <rect x="0.4" y="0.4" width="981.2" height="701.2"/>
        <line x1="0" y1="9.5" x2="982" y2="9.5"/>
        <line x1="0" y1="692.5" x2="982" y2="692.5"/>
        <line x1="9.5" y1="0" x2="9.5" y2="702"/>
        <line x1="972.5" y1="0" x2="972.5" y2="702"/>
        <line x1="464" y1="0" x2="464" y2="702"/>
        <line x1="517" y1="0" x2="517" y2="702"/>
      </g>
    </svg>
  </div>
</body>
</html>
```